High End Craft Beer needs a label design update

We would like to update the design of our line of craft beer, named Louis-Benoît. The brand name needs to stay predominant in the design. We initially launched with 2 flavours, but with the addition of the third product, we feel there is not enough differentiation between each flavour, and customers are confused in which flavour they are buying (BELGIAN WHITE, INDIA PALE ALE, and AMBER ALE are the current flavours).

We plan to launch a BLONDE LAGER product, but need the 4 products to be more differentiated between each other.

We are looking for the design of the 3 current products (and also the BLOND LAGER if possible) that would be more differentiated.
Updates

Reason: Hello, I am still looking for options, so I am extending the dead-line by 5 days. Thanks

Target Market(s)

Males (75%), 21 to 40.

Font styles to use
Serif
Sans Serif

Requirements
Must have
• All 4 labels need to be coherent between themselves, but more differentiated than the current design
Should not have
• We don't want to completely "re-brand" the product, as customers currently really like the products and its design. And current customers need to easily "recognize" the product they like at store level. The only problem is the confusion between the flavours.

```html
<!DOCTYPE html>
<html lang="fr">
<head>
<meta charset="utf-8">
<title>Louis-Benoît — étiquettes</title>
<link rel="stylesheet" href="https://fonts.googleapis.com/css2?family=Oswald:wght@400;500;600;700&family=Libre+Baskerville:wght@400;700&display=swap">
<style>
  :root {
    --ink: #2b2b2b;
    --paper: #ffffff;
    --amber: #d9773a;
    --amber-line: #c9703e;
    --silver: #b9b9b9;
    --silver-soft: #d0d0d0;
    --green: #1f5c3e;
    --green-soft: #2f6e4e;
    --muted: #777777;
    --ornament-amber: linear-gradient(180deg, #e7b08c, #c9704a);
    --ornament-silver: linear-gradient(180deg, #e6e6e6, #bdbdbd);
    --ornament-green: linear-gradient(180deg, #5e8d74, #1f5c3e);
  }
  * { box-sizing: border-box; margin: 0; padding: 0; }
  html, body { width: 935px; height: 1200px; overflow: hidden; background: var(--paper); }
  .canvas { position: relative; width: 935px; height: 1200px; }

  .label { position: absolute; width: 286px; height: 455px; text-align: center; color: var(--ink); }
  .label-shape { position: absolute; inset: 0; width: 100%; height: 100%; }
  .label-body { position: absolute; inset: 0; }

  .crest { position: absolute; left: 50%; transform: translateX(-50%); top: 18px; width: 150px; height: 112px;
           clip-path: polygon(50% 0, 62% 40%, 100% 55%, 100% 100%, 0 100%, 0 55%, 38% 40%); opacity: .85; }
  .foot-ornament { position: absolute; left: 50%; transform: translateX(-50%); top: 394px; width: 110px; height: 32px;
                   clip-path: polygon(0 0, 100% 0, 60% 50%, 50% 100%, 40% 50%); opacity: .85; }

  .brewery { position: absolute; top: 144px; width: 100%; font: 400 8px/1 "Libre Baskerville", serif; letter-spacing: 1px; color: var(--muted); }
  .brand { position: absolute; top: 160px; width: 100%; font: 600 48px/60px "Oswald", sans-serif; letter-spacing: 7px; text-transform: uppercase; }
  .brand span { display: block; }
  .flavour { position: absolute; top: 286px; width: 100%; font: 500 20px/1 "Oswald", sans-serif; letter-spacing: 1px; text-transform: uppercase; }
  .origin { position: absolute; top: 314px; width: 100%; font: 400 12px/1 "Libre Baskerville", serif; letter-spacing: 1.5px; }
  .specs { position: absolute; top: 334px; left: 26px; right: 22px; display: flex; align-items: center; justify-content: space-between; }
  .specs .kind { font: 700 10px/11px "Oswald", sans-serif; text-align: left; letter-spacing: .5px; }
  .specs .volume { font: 600 19px/1 "Oswald", sans-serif; }
  .specs .abv { font: 600 10px/9px "Oswald", sans-serif; text-align: left; }
  .specs .abv small { display: block; font-size: 5px; }

  .label--amber { left: 22px; top: 380px; }
  .label--amber .flavour { color: var(--amber); }
  .label--amber .crest, .label--amber .foot-ornament { background: var(--ornament-amber); }

  .label--blanche { left: 320px; top: 372px; }
  .label--blanche .flavour { color: var(--silver-soft); letter-spacing: 2px; }
  .label--blanche .crest, .label--blanche .foot-ornament { background: var(--ornament-silver); }
  .label--blanche .specs { left: 38px; right: 34px; }

  .label--ipa { left: 616px; top: 364px; width: 296px; height: 470px; }
  .label--ipa .crest { background: var(--ornament-green); top: 24px; }
  .label--ipa .foot-ornament { background: var(--ornament-green); top: 384px; width: 70px; }
  .label--ipa .brewery { top: 146px; color: var(--green-soft); }
  .label--ipa .brand { top: 162px; font-size: 46px; line-height: 56px; }
  .ribbon { position: absolute; top: 282px; left: 14px; right: 14px; height: 30px; }
  .ribbon span { position: absolute; inset: 0; display: flex; align-items: center; justify-content: center;
                 font: 700 17px/1 "Libre Baskerville", serif; color: var(--paper); letter-spacing: 1px; }
  .label--ipa .origin { top: 324px; color: var(--green); }
  .ipa-kind { position: absolute; top: 342px; width: 100%; font: 700 10px/1 "Libre Baskerville", serif; letter-spacing: .5px; }
  .ipa-volume { position: absolute; top: 386px; left: 34px; font: 600 13px/1 "Oswald", sans-serif; }
  .ipa-abv { position: absolute; top: 380px; right: 34px; font: 600 12px/11px "Oswald", sans-serif; text-align: left; }
  .ipa-abv small { display: block; font-size: 5px; }
  .corner-tag { position: absolute; top: 26px; font: 700 12px/1 "Libre Baskerville", serif; color: var(--paper); }
  .corner-tag--left { left: 16px; transform: rotate(-45deg); }
  .corner-tag--right { right: 16px; transform: rotate(45deg); }
</style>
</head>
<body>
<main class="canvas">

  <article class="label label--amber">
    <svg class="label-shape" viewBox="0 0 286 455" aria-hidden="true">
      <path d="M1 1 H285 V380 Q205 400 143 453 Q81 400 1 380 Z" fill="var(--paper)" stroke="var(--amber-line)" stroke-width="2"/>
    </svg>
    <div class="label-body">
      <div class="crest" role="img" aria-label="Ornamental crest in copper"></div>
      <p class="brewery">· BRASSERIE DEUX RIVES ·</p>
      <h2 class="brand"><span>Louis</span><span>Benoît</span></h2>
      <p class="flavour">Amber Ale Ambrée</p>
      <p class="origin">BRASSÉE AU QUÉBEC</p>
      <div class="specs">
        <p class="kind">BIÈRE FORTE<br>STRONG BEER</p>
        <p class="volume">500 ML</p>
        <p class="abv">6.2%<small>ALC. VOL.</small></p>
      </div>
      <div class="foot-ornament" role="img" aria-label="Small copper flourish"></div>
    </div>
  </article>

  <article class="label label--blanche">
    <svg class="label-shape" viewBox="0 0 286 455" aria-hidden="true">
      <path d="M1 1 H285 V380 Q205 400 143 453 Q81 400 1 380 Z" fill="var(--paper)" stroke="var(--silver)" stroke-width="2"/>
    </svg>
    <div class="label-body">
      <div class="crest" role="img" aria-label="Ornamental crest in silver foil"></div>
      <p class="brewery">· BRASSERIE DEUX RIVES ·</p>
      <h2 class="brand"><span>Louis</span><span>Benoît</span></h2>
      <p class="flavour">Blanche · White</p>
      <p class="origin">BRASSÉE AU QUÉBEC</p>
      <div class="specs">
        <p class="kind">BIÈRE<br>BEER</p>
        <p class="volume">500 ML</p>
        <p class="abv">5.1%<small>ALC. VOL.</small></p>
      </div>
      <div class="foot-ornament" role="img" aria-label="Small silver flourish"></div>
    </div>
  </article>

  <article class="label label--ipa">
    <svg class="label-shape" viewBox="0 0 296 470" aria-hidden="true">
      <path d="M0 0 H296 V392 L148 470 L0 392 Z" fill="var(--green)"/>
      <path d="M8 8 H288 V387 L148 461 L8 387 Z" fill="var(--paper)"/>
      <path d="M13 13 H283 V384 L148 455 L13 384 Z" fill="none" stroke="var(--green)" stroke-width="1.5"/>
      <path d="M8 8 H60 L8 60 Z" fill="var(--green)"/>
      <path d="M288 8 H236 L288 60 Z" fill="var(--green)"/>
      <path d="M0 288 H22 L14 297 L22 306 H0 Z M296 288 H274 L282 297 L274 306 H296 Z" fill="var(--green)"/>
    </svg>
    <div class="label-body">
      <span class="corner-tag corner-tag--left">IPA</span>
      <span class="corner-tag corner-tag--right">IPA</span>
      <div class="crest" role="img" aria-label="Ornamental crest in green"></div>
      <p class="brewery">· BRASSERIE DEUX RIVES ·</p>
      <h2 class="brand"><span>Louis</span><span>Benoît</span></h2>
      <div class="ribbon">
        <svg viewBox="0 0 268 30" width="268" height="30" aria-hidden="true">
          <path d="M12 0 H256 V30 H12 Z" fill="var(--green)"/>
        </svg>
        <span>INDIA PALE ALE</span>
      </div>
      <p class="origin">BRASSÉE AU QUÉBEC</p>
      <p class="ipa-kind">BIÈRE FORTE STRONG BEER</p>
      <p class="ipa-volume">500 ML</p>
      <p class="ipa-abv">6.2%<small>ALC. VOL.</small></p>
      <div class="foot-ornament" role="img" aria-label="Small green flourish"></div>
    </div>
  </article>

</main>
</body>
</html>
```